Business Card Design

Personal training studio. My colors are burnt orange and grey. Specializing in group training and total body composition change. Nutritional consultant and contest prep.

Target Market(s)

My audience are people who are looking for total body composition change as well as knowledge on how to effectively receive results in the gym that they are a member of.

Industry/Entity Type

Training

Contact Information for Business Card

Dr. Maris Thackery
Marisjthackery@plumvane.com
3129071436
2815 west Brell ave.
Harrowfield Ohio 43219

Colors
f37122
aaaaaa

Requirements
Must have
• Animphasis on gaining knowledge that will sustain them for a life time. Healthy results and notice me results.
Nice to have
• Card should correlate with the colors of the studio. Orange and grey. With black flooring with orange speckles in it.

```html
<!DOCTYPE html>
<html lang="en">
<head>
<meta charset="utf-8">
<title>Kestrel Yard Fitness – Business Card</title>
<link rel="stylesheet" href="https://fonts.googleapis.com/css2?family=Open+Sans:wght@400;600&family=Montserrat:wght@600&display=swap">
<style>
  :root {
    --burnt-orange: #f37122;
    --grey: #aaaaaa;
    --card-black: #141414;
    --card-black-light: #2a2a2a;
    --backdrop: #e4e1dd;
    --text-light: #d8d8d8;
  }
  * { margin: 0; padding: 0; box-sizing: border-box; }
  html, body { width: 1200px; height: 913px; overflow: hidden; }
  body {
    background: var(--backdrop);
    font-family: "Open Sans", Arial, sans-serif;
    position: relative;
  }
  .card {
    position: absolute;
    width: 525px;
    height: 300px;
    border-radius: 4px;
    background: linear-gradient(135deg, var(--card-black-light) 0%, var(--card-black) 55%, #0b0b0b 100%);
    box-shadow: 0 6px 18px rgba(0,0,0,0.25);
    overflow: hidden;
  }
  .card--front { left: 45px; top: 306px; }
  .card--back { left: 630px; top: 306px; }

  .brand {
    position: absolute;
    display: flex;
    align-items: center;
    gap: 12px;
  }
  .brand__dot {
    width: 30px; height: 30px;
    border-radius: 50%;
    background: var(--burnt-orange);
    flex: none;
  }
  .brand__name {
    font-family: "Montserrat", Arial, sans-serif;
    font-weight: 600;
    color: var(--grey);
    letter-spacing: 1px;
    text-transform: uppercase;
    white-space: nowrap;
  }
  .card--front .brand { left: 50%; top: 50%; transform: translate(-50%, -50%); }
  .card--front .brand__name { font-size: 26px; }
  .card--front .brand__dot { width: 40px; height: 40px; }

  .card--back .brand { right: 34px; top: 38px; }
  .card--back .brand__name { font-size: 17px; }

  .name-tab {
    position: absolute;
    left: 0; top: 108px;
    width: 260px; height: 44px;
    background: var(--burnt-orange);
    border-radius: 0 8px 8px 0;
    display: flex; align-items: center;
    padding-left: 30px;
  }
  .name-tab__text {
    font-family: "Montserrat", Arial, sans-serif;
    font-weight: 600;
    font-size: 17px;
    color: #1a1a1a;
  }
  .contact-frame {
    position: absolute;
    left: 30px; right: 24px;
    top: 96px; bottom: 24px;
    border: 1px solid var(--burnt-orange);
    opacity: 0.85;
  }
  .contact {
    position: absolute;
    color: var(--text-light);
    font-size: 12px;
    line-height: 1.45;
    display: flex; gap: 8px; align-items: flex-start;
  }
  .contact svg { flex: none; margin-top: 2px; }
  .contact--phone { right: 48px; top: 116px; }
  .contact--address { left: 46px; bottom: 62px; }
  .contact--email { left: 46px; bottom: 38px; }
</style>
</head>
<body>
  <section class="card card--front" aria-label="Card front">
    <div class="brand">
      <span class="brand__dot"></span>
      <span class="brand__name">Kestrel Yard Fitness</span>
    </div>
  </section>

  <section class="card card--back" aria-label="Card back">
    <div class="contact-frame"></div>
    <div class="brand">
      <span class="brand__dot"></span>
      <span class="brand__name">Kestrel Yard Fitness</span>
    </div>
    <div class="name-tab"><span class="name-tab__text">Dr. Maris Thackery</span></div>

    <div class="contact contact--phone">
      <svg width="12" height="12" viewBox="0 0 24 24" aria-hidden="true"><path fill="#f37122" d="M6.6 10.8a15.1 15.1 0 0 0 6.6 6.6l2.2-2.2a1 1 0 0 1 1-.25 11.4 11.4 0 0 0 3.6.57 1 1 0 0 1 1 1V20a1 1 0 0 1-1 1A17 17 0 0 1 3 4a1 1 0 0 1 1-1h3.5a1 1 0 0 1 1 1c0 1.25.2 2.45.57 3.57a1 1 0 0 1-.25 1z"/></svg>
      <span>3129071436</span>
    </div>
    <div class="contact contact--address">
      <svg width="11" height="13" viewBox="0 0 24 28" aria-hidden="true"><path fill="#f37122" d="M12 0a10 10 0 0 0-10 10c0 7.5 10 18 10 18s10-10.5 10-18A10 10 0 0 0 12 0zm0 14a4 4 0 1 1 0-8 4 4 0 0 1 0 8z"/></svg>
      <span>2815 west Brell ave. Harrowfield<br>Ohio 43219</span>
    </div>
    <div class="contact contact--email">
      <svg width="13" height="10" viewBox="0 0 26 20" aria-hidden="true"><rect width="26" height="20" rx="2" fill="#f37122"/><path d="M1 2l12 9 12-9" stroke="#141414" stroke-width="2" fill="none"/></svg>
      <span>Marisjthackery@plumvane.com</span>
    </div>
  </section>
</body>
</html>
```